Quillstone Business Card

We need a business card design. We have a logo from a previous Sketchfold project and I am attaching the logo files in jpeg and photoshop.

```html
<!DOCTYPE html>
<html lang="en">
<head>
<meta charset="utf-8">
<title>Quillstone Business Card</title>
<link rel="stylesheet" href="https://fonts.googleapis.com/css2?family=Arimo:wght@400;700&display=swap">
<style>
  :root {
    --paper: #fcfcfa;
    --band: #c2c2c2;
    --band-edge: #e4e4e2;
    --ink: #111111;
    --brand-dark: #434343;
    --brand-green: #5db531;
  }
  * { margin: 0; padding: 0; box-sizing: border-box; }
  html, body {
    width: 720px;
    height: 1200px;
    overflow: hidden;
    background: var(--paper);
  }
  .card {
    position: relative;
    width: 720px;
    height: 1200px;
    background: var(--paper);
    font-family: "Arimo", Arial, sans-serif;
    color: var(--ink);
  }
  .side-band {
    position: absolute;
    left: 0; top: 0;
    width: 78px; height: 1200px;
    background: var(--band);
  }
  .side-band-edge {
    position: absolute;
    left: 78px; top: 0;
    width: 15px; height: 1200px;
    background: var(--band-edge);
  }
  .brand-name {
    position: absolute;
    left: 160px;
    top: 324px;
    font-size: 82px;
    font-weight: 700;
    letter-spacing: -3px;
    line-height: 1;
    color: var(--brand-dark);
  }
  .person-name {
    position: absolute;
    left: 174px;
    top: 532px;
    font-size: 46px;
    font-weight: 400;
    line-height: 1;
  }
  .person-role {
    position: absolute;
    left: 249px;
    top: 594px;
    font-size: 28px;
    line-height: 1;
    color: var(--brand-green);
  }
  .contact-row {
    position: absolute;
    left: 162px;
    display: flex;
    align-items: center;
    font-size: 28px;
    line-height: 1;
  }
  .contact-row svg {
    width: 30px;
    height: 30px;
    fill: var(--brand-green);
    flex: none;
  }
  .contact-row span { margin-left: 32px; }
  .row-web   { top: 698px; }
  .row-mail  { top: 743px; }
  .row-phone { top: 841px; }
  .row-fax   { top: 886px; }
  .address-pin {
    position: absolute;
    left: 162px;
    top: 974px;
    width: 26px;
    height: 38px;
    fill: var(--brand-green);
  }
  .address {
    position: absolute;
    left: 229px;
    top: 988px;
    font-size: 28px;
    line-height: 27px;
    letter-spacing: -1.6px;
    text-transform: uppercase;
  }
</style>
</head>
<body>
<main class="card">
  <div class="side-band"></div>
  <div class="side-band-edge"></div>

  <div class="brand-name">Quillstone</div>

  <h1 class="person-name">Ravin K</h1>
  <p class="person-role">Designer</p>

  <div class="contact-row row-web">
    <svg viewBox="0 0 30 30" aria-hidden="true">
      <circle cx="15" cy="15" r="14"/>
      <path d="M8 8c3 1 4 4 7 4s2 4 0 5-4 1-4 4-3 1-4-2 0-4-1-6 1-4 2-5zM19 18c2-1 5 0 5 2s-3 4-5 4-2-5 0-6z" fill="#fcfcfa"/>
    </svg>
    <span>www.yourwebsite.com</span>
  </div>
  <div class="contact-row row-mail">
    <svg viewBox="0 0 30 30" aria-hidden="true">
      <path d="M2 7h26v17H2zM5 10v11h20V10l-10 8zM7 9.5l8 6.5 8-6.5z" fill-rule="evenodd"/>
    </svg>
    <span>ravin@email.com</span>
  </div>
  <div class="contact-row row-phone">
    <svg viewBox="0 0 30 30" aria-hidden="true">
      <path d="M9 2h6l1 7-4 1v10l4 1-1 7H9c-3-4-4-8-4-13S6 6 9 2z"/>
    </svg>
    <span>+91 123456789</span>
  </div>
  <div class="contact-row row-fax">
    <svg viewBox="0 0 30 30" aria-hidden="true">
      <path d="M8 2h14v9H8zM10 4v2h10V4zM10 7v2h10V7zM2 13h26v10H2zM4 25h22v4H4z" fill-rule="evenodd"/>
    </svg>
    <span>+91 123456789</span>
  </div>

  <svg class="address-pin" viewBox="0 0 26 38" aria-hidden="true">
    <path d="M13 0C6 0 0 5 0 12c0 8 13 26 13 26s13-18 13-26C26 5 20 0 13 0zm0 7a5 5 0 1 1 0 10 5 5 0 0 1 0-10z" fill-rule="evenodd"/>
  </svg>
  <address class="address" style="font-style:normal">
    Business Name<br>
    1234 Street Name<br>
    City, State 12345
  </address>
</main>
</body>
</html>
```